Course Graduation Certificate

This project is not for a flyer but instead for the creation of a course graduation certificate. The final certificate needs to include the Marlowe Summit Aviation Academy logo and the text stating as follows:
Certifies that ___________________________ has satisfactorily completed the course of _______________________________ on ________________________________
I would also like to include some type of gold seal of completion as well as a place to sign my name and credentials at the bottom of the certificate
I have included the Marlowe Summit Aviation Academy logo as well as three other certificate examples for you to work from.
Target Market(s)
Students completing a certification course and receiving a certificate
Look and feel

```html
<!DOCTYPE html>
<html lang="en">
<head>
<meta charset="utf-8">
<title>Course Graduation Certificate – Marlowe Summit Aviation Academy</title>
<link rel="stylesheet" href="https://fonts.googleapis.com/css2?family=Michroma&family=Cinzel:wght@400;500&family=Great+Vibes&display=swap">
<style>
  :root {
    --navy: #1d2f50;
    --cream: #f8f5ea;
    --gold-light: #f1d28a;
    --gold: #c8973f;
    --gold-dark: #8a5f1d;
    --title-gold: #b8a777;
    --title-gold-strong: #c9b988;
    --seal-light: #eed59a;
    --seal-mid: #caa158;
    --seal-deep: #a67a34;
    --ink: #2b2b2b;
    --rule: #555555;
    --backdrop: #e9e9e9;
  }
  * { margin: 0; padding: 0; box-sizing: border-box; }
  html, body { width: 1200px; height: 912px; overflow: hidden; background: var(--backdrop); }
  .certificate {
    position: relative;
    width: 1200px;
    height: 912px;
    background: var(--cream);
    overflow: hidden;
    color: var(--ink);
  }
  .certificate__frame { position: absolute; inset: 0; }
  .certificate__title {
    position: absolute;
    top: 136px;
    left: 0;
    width: 1200px;
    text-align: center;
    font-family: "Michroma", sans-serif;
    font-weight: 400;
    font-size: 40px;
    letter-spacing: 5px;
    color: var(--title-gold);
  }
  .certificate__title strong { font-weight: 400; color: var(--title-gold-strong); text-shadow: 0 0 1px var(--title-gold-strong); }
  .seal-placeholder {
    position: absolute;
    left: 480px;
    top: 268px;
    width: 180px;
    height: 180px;
    border-radius: 50%;
    background: radial-gradient(circle at 40% 35%, var(--seal-light) 0%, var(--seal-mid) 60%, var(--seal-deep) 100%);
  }
  .body-text {
    position: absolute;
    left: 300px;
    width: 540px;
    text-align: center;
    font-family: "Cinzel", serif;
    font-size: 16px;
    letter-spacing: 1.5px;
  }
  .script {
    position: absolute;
    font-family: "Great Vibes", cursive;
    font-size: 44px;
    line-height: 1;
    word-spacing: 10px;
    color: var(--ink);
    text-align: center;
    white-space: nowrap;
  }
  .rule { position: absolute; height: 1px; background: var(--rule); }
  .line-label { top: 472px; }
  .recipient { left: 320px; width: 500px; top: 500px; }
  .rule--recipient { left: 360px; width: 420px; top: 556px; }
  .line-course { top: 582px; }
  .course { left: 320px; width: 500px; top: 612px; }
  .rule--course { left: 360px; width: 420px; top: 668px; }
  .date-row { position: absolute; left: 340px; width: 460px; top: 714px; display: flex; align-items: baseline; justify-content: center; gap: 16px; }
  .date-row__label { font-family: "Cinzel", serif; font-size: 16px; letter-spacing: 1.5px; }
  .date-row__value { font-family: "Great Vibes", cursive; font-size: 38px; word-spacing: 8px; white-space: nowrap; }
  .rule--date { left: 360px; width: 420px; top: 772px; }
  .signatory { position: absolute; left: 880px; width: 260px; top: 690px; text-align: center; }
  .signatory__rule { height: 1px; background: var(--rule); margin-bottom: 10px; }
  .signatory__label { font-family: "Cinzel", serif; font-size: 14px; letter-spacing: 1.5px; }
  .signatory__name { font-family: "Great Vibes", cursive; font-size: 38px; line-height: 1.1; word-spacing: 8px; margin-top: 6px; white-space: nowrap; }
  .academy-mark { position: absolute; left: 70px; top: 812px; display: flex; align-items: center; gap: 12px; }
  .academy-mark__square { width: 22px; height: 22px; background: var(--navy); }
  .academy-mark__name { font-family: "Cinzel", serif; font-size: 18px; font-weight: 500; letter-spacing: 1.5px; color: var(--navy); }
</style>
</head>
<body>
<main class="certificate">
  <svg class="certificate__frame" width="1200" height="912" viewBox="0 0 1200 912" aria-hidden="true">
    <defs>
      <linearGradient id="goldBand" x1="0" y1="0" x2="1" y2="0">
        <stop offset="0" stop-color="#8a5f1d"/>
        <stop offset="0.3" stop-color="#f1d28a"/>
        <stop offset="0.55" stop-color="#c8973f"/>
        <stop offset="0.8" stop-color="#f1d28a"/>
        <stop offset="1" stop-color="#8a5f1d"/>
      </linearGradient>
    </defs>
    <path class="header-gold" fill="url(#goldBand)" d="M0 0 H1200 V304 L690 336 C640 342 625 378 570 378 C515 378 500 342 450 336 L0 318 Z"/>
    <path class="header-navy" fill="#1d2f50" d="M0 0 H1200 V292 L690 324 C640 330 625 366 570 366 C515 366 500 330 450 324 L0 306 Z"/>
    <rect class="footer-gold" x="0" y="900" width="1200" height="6" fill="url(#goldBand)"/>
  </svg>

  <h1 class="certificate__title">CERTIFICATE OF <strong>COMPLETION</strong></h1>

  <div class="seal-placeholder" role="img" aria-label="Gold seal of completion"></div>

  <p class="body-text line-label">CERTIFIES THAT</p>
  <p class="script recipient">Owen Hartley</p>
  <div class="rule rule--recipient"></div>

  <p class="body-text line-course">HAS SATISFACTORILY COMPLETED THE COURSE OF</p>
  <p class="script course">Course Name</p>
  <div class="rule rule--course"></div>

  <div class="date-row">
    <span class="date-row__label">ON</span>
    <span class="date-row__value">25th day of July, 2025</span>
  </div>
  <div class="rule rule--date"></div>

  <div class="signatory">
    <div class="signatory__rule"></div>
    <p class="signatory__label">AUTHORIZED SIGNATORY</p>
    <p class="signatory__name">Name Name</p>
  </div>

  <div class="academy-mark">
    <span class="academy-mark__square"></span>
    <span class="academy-mark__name">Marlowe Summit Aviation Academy</span>
  </div>
</main>
</body>
</html>
```